Varemo Group Business Card Design

The CEO is looking for a new trendy look for his business card.
You can stay with current branding or come up with something new/creative. It can be 3D, including Medical Office buildings. You can use our logo in a variety of colors. Please include name, title, company name, company website, email address, cell number

Target Market(s)

Real Estate Development and Construction

Industry/Entity Type

Health care real estate

Contact Information for Business Card

Rohesh Kumbar, CEO M-727.418.9062 E-roheshkumbar@varemo.com Address:4100 Lindell Ave, Tampa, FL 33611 www.varemo.com

Font styles to use
Other font styles liked:
• Be creative

Requirements
Must have
• Creative, trendy look
Nice to have
• Please go to our website to get a feel- www. varemo.com
Should not have
• small fonts

```html
<!DOCTYPE html>
<html lang="en">
<head>
<meta charset="UTF-8">
<title>Varemo Group Business Card</title>
<link href="https://fonts.googleapis.com/css2?family=Poppins:wght@500;600;700;800&display=swap" rel="stylesheet">
<style>
  :root {
    --page: #ffffff;
    --red-edge: #a80006;
    --red-mid: #6a0004;
    --panel-dark: #1e0002;
    --panel-core: #2c0003;
    --ink: #ffffff;
    --rule: rgba(255,255,255,0.55);
  }
  * { margin: 0; padding: 0; box-sizing: border-box; }
  html, body { width: 1038px; height: 1200px; overflow: hidden; background: var(--page); }
  .sheet {
    position: relative;
    width: 1090px; height: 1260px;
    transform: scale(0.9523);
    transform-origin: 0 0;
    font-family: "Poppins", sans-serif;
    color: var(--ink);
  }
  .card {
    position: absolute;
    left: 20px;
    width: 1050px; height: 600px;
    overflow: hidden;
  }
  .card--front { top: 22px; }
  .card--back { top: 642px; }
  .card__backdrop {
    position: absolute; inset: 0;
    background: radial-gradient(ellipse 70% 62% at 50% 50%,
      var(--panel-core) 0%, var(--panel-dark) 55%, var(--red-mid) 82%, var(--red-edge) 100%);
  }
  .brand {
    position: absolute;
    font-weight: 800;
    line-height: 0.9;
    text-align: right;
    letter-spacing: -2px;
  }
  .brand span { display: block; }
  .brand--front { left: 270px; width: 545px; top: 205px; font-size: 140px; }
  .brand--front .brand__sub { font-size: 60px; letter-spacing: 0; margin-top: 8px; }
  .brand--back { left: 45px; width: 350px; top: 245px; font-size: 84px; }
  .brand--back .brand__sub { font-size: 36px; letter-spacing: 0; margin-top: 2px; }
  .divider {
    position: absolute;
    left: 397px; top: 148px;
    width: 1.5px; height: 328px;
    background: var(--rule);
  }
  .person { position: absolute; left: 422px; top: 142px; }
  .person__name { font-size: 58px; font-weight: 800; letter-spacing: 6px; line-height: 1; }
  .person__title { font-size: 26px; font-weight: 700; letter-spacing: 1.8px; margin-top: 14px; }
  .contacts { position: absolute; left: 420px; top: 285px; list-style: none; }
  .contacts li {
    display: flex; align-items: center;
    height: 52px;
    font-size: 28px; font-weight: 500; letter-spacing: 2.4px;
  }
  .contacts svg { width: 36px; height: 36px; margin-right: 18px; flex: none; }
</style>
</head>
<body>
<div class="sheet">

  <section class="card card--front">
    <div class="card__backdrop" role="img" aria-label="Layered angular red ribbons framing a dark central panel"></div>
    <div class="brand brand--front"><span>Varemo</span><span class="brand__sub">Group</span></div>
  </section>

  <section class="card card--back">
    <div class="card__backdrop" role="img" aria-label="Layered angular red ribbons framing a dark central panel"></div>

    <div class="brand brand--back"><span>Varemo</span><span class="brand__sub">Group</span></div>
    <div class="divider"></div>

    <div class="person">
      <h1 class="person__name">ROHESH KUMBAR</h1>
      <p class="person__title">Chief Executive Officer</p>
    </div>

    <ul class="contacts">
      <li>
        <svg viewBox="0 0 24 24" fill="#fff"><path d="M6.6 10.8a15 15 0 0 0 6.6 6.6l2.2-2.2c.3-.3.7-.4 1-.2 1.1.4 2.3.6 3.6.6.6 0 1 .4 1 1V20c0 .6-.4 1-1 1A17 17 0 0 1 3 4c0-.6.4-1 1-1h3.5c.6 0 1 .4 1 1 0 1.3.2 2.5.6 3.6.1.3 0 .7-.2 1z"/><path d="M14 3a7 7 0 0 1 7 7h-2a5 5 0 0 0-5-5zm0 3.5a3.5 3.5 0 0 1 3.5 3.5h-2A1.5 1.5 0 0 0 14 8.5z"/></svg>
        (727) 418-9062
      </li>
      <li>
        <svg viewBox="0 0 24 24" fill="#fff"><path d="M3 5h18c.6 0 1 .4 1 1v12c0 .6-.4 1-1 1H3c-.6 0-1-.4-1-1V6c0-.6.4-1 1-1zm1 3v1l8 5 8-5V8l-8 5z"/></svg>
        roheshkumbar@varemo.com
      </li>
      <li>
        <svg viewBox="0 0 24 24" fill="#fff"><path d="M12 2a7 7 0 0 1 7 7c0 5-7 13-7 13S5 14 5 9a7 7 0 0 1 7-7zm0 4a3 3 0 1 0 0 6 3 3 0 0 0 0-6z"/></svg>
        4100 Lindell Ave, Tampa, FL 33611
      </li>
      <li>
        <svg viewBox="0 0 24 24" fill="none" stroke="#fff" stroke-width="2"><circle cx="12" cy="12" r="9"/><path d="M3 12h18M12 3c3 3 3 15 0 18M12 3c-3 3-3 15 0 18"/></svg>
        www.varemo.com
      </li>
    </ul>
  </section>

</div>
</body>
</html>
```